Crestline Lending Group Business Cards

We are looking to revamp the current business cards each of our locations uses. We are a lending company that specializes in personal loans, title loans, and tax services. We have locations in New Mexico, Texas, and Oklahoma.

We would like a cleaner, sleeker look while still highlighting what we offer. Title Loans, Personal Loans & Tax Services. We also want to include our referral fee somewhere on the card. We would like to see an English option as well as a Spanish option for the cards.

PLEASE NOTE: Some business cards do not include the employee's name but just the store's location, while others will include both.

These are double-sided business cards, and we would like to see proof if possible. I have included proofs of our current business cards for you to review below, as well as our company logo. Feel free to get creative with the logo, etc! Colors should match the logo; however, you do not need to use all of our logo colors if you don't want to.

```html
<!DOCTYPE html>
<html lang="en">
<head>
<meta charset="utf-8">
<title>Crestline Lending Group — Business Cards</title>
<link rel="stylesheet" href="https://fonts.googleapis.com/css2?family=Open+Sans:wght@400;600;700;800&display=swap">
<style>
  :root {
    --backdrop: #232323;
    --card: #1e1e21;
    --card-edge: #2b2b2f;
    --green: #1d5e2f;
    --red: #d0282b;
    --red-bright: #ee1c25;
    --white: #f2f2f2;
  }
  * { box-sizing: border-box; margin: 0; padding: 0; }
  html, body { width: 1200px; height: 780px; overflow: hidden; }
  body {
    background: var(--backdrop);
    font-family: "Open Sans", Arial, sans-serif;
    color: var(--white);
    display: flex;
    align-items: center;
    justify-content: center;
    gap: 40px;
  }
  .card {
    position: relative;
    width: 540px;
    height: 310px;
    background: var(--card);
    border: 1px solid var(--card-edge);
    border-radius: 4px;
    box-shadow: 0 18px 40px rgba(0,0,0,.45);
    overflow: hidden;
  }

  /* brand name set in type */
  .brand {
    display: flex;
    align-items: center;
    gap: 10px;
    white-space: nowrap;
  }
  .brand-dot {
    width: 14px; height: 14px;
    border-radius: 50%;
    background: var(--red);
    flex: none;
  }
  .brand-name {
    font-weight: 700;
    color: var(--green);
    letter-spacing: .5px;
    line-height: 1.1;
  }

  /* front */
  .card-front .brand { position: absolute; top: 34px; right: 40px; }
  .card-front .brand-name { font-size: 24px; }
  .addresses {
    position: absolute;
    top: 96px; left: 34px;
    font-size: 13px;
    line-height: 1.45;
  }
  .addresses p + p { margin-top: 8px; }
  .contacts {
    position: absolute;
    top: 196px; left: 34px;
    list-style: none;
    font-size: 13px;
    line-height: 1.6;
  }
  .contacts li { display: flex; align-items: center; gap: 8px; }
  .contacts svg { width: 12px; height: 12px; fill: var(--red); flex: none; }
  .person {
    position: absolute;
    right: 44px; bottom: 40px;
    text-align: right;
  }
  .person-name { font-size: 26px; font-weight: 700; line-height: 1.1; }
  .person-name .first { color: var(--red); }
  .person-name .last { color: var(--green); }
  .person-title { font-size: 15px; margin-top: 2px; }
  .edge-tab {
    position: absolute;
    right: 0; bottom: 36px;
    width: 18px; height: 50px;
    background: var(--red-bright);
  }

  /* back */
  .card-back .brand {
    position: absolute;
    top: 50px; left: 0; right: 0;
    justify-content: center;
  }
  .card-back .brand-name { font-size: 28px; }
  .referral {
    position: absolute;
    left: 58px; top: 150px;
  }
  .referral-lead { font-size: 15px; }
  .referral-offer { display: flex; align-items: flex-end; gap: 6px; margin-top: 2px; }
  .referral-get { font-size: 30px; font-weight: 800; color: var(--green); line-height: 1; }
  .referral-upto { font-size: 10px; font-weight: 700; color: var(--green); line-height: 1.1; padding-bottom: 3px; }
  .referral-amount { font-size: 40px; font-weight: 800; color: var(--red); line-height: 1; margin-top: 2px; }
  .divider {
    position: absolute;
    left: 262px; top: 150px;
    width: 1px; height: 110px;
    background: var(--white);
  }
  .services {
    position: absolute;
    left: 296px; top: 150px;
  }
  .services-title { font-size: 15px; letter-spacing: .5px; }
  .services ul { list-style: none; margin-top: 4px; }
  .services li {
    font-size: 17px;
    line-height: 1.4;
    display: flex; align-items: center; gap: 8px;
  }
  .services li::before {
    content: "";
    width: 9px; height: 9px;
    border-radius: 50%;
    background: var(--green);
  }
</style>
</head>
<body>

  <section class="card card-front" aria-label="Card front">
    <div class="brand">
      <span class="brand-dot"></span>
      <span class="brand-name">Crestline Lending Group</span>
    </div>

    <div class="addresses">
      <p>418 Cedar Avenue, Suite B,<br>Riverton, Texas 79010</p>
      <p>92 Mesa Road<br>Riverton, Texas 79010</p>
    </div>

    <ul class="contacts">
      <li>
        <svg viewBox="0 0 24 24" aria-hidden="true"><path d="M6.6 10.8a15.1 15.1 0 0 0 6.6 6.6l2.2-2.2a1 1 0 0 1 1-.25 11.4 11.4 0 0 0 3.6.57 1 1 0 0 1 1 1V20a1 1 0 0 1-1 1A17 17 0 0 1 3 4a1 1 0 0 1 1-1h3.5a1 1 0 0 1 1 1c0 1.25.2 2.45.57 3.57a1 1 0 0 1-.25 1z"/></svg>
        (505) 014-2736
      </li>
      <li>
        <svg viewBox="0 0 24 24" aria-hidden="true"><path d="M12 2a10 10 0 1 0 0 20 10 10 0 0 0 0-20zm6.9 6h-2.9a15.7 15.7 0 0 0-1.4-3.6A8 8 0 0 1 18.9 8zM12 4a14 14 0 0 1 1.9 4h-3.8A14 14 0 0 1 12 4zM4.3 14a8 8 0 0 1 0-4h3.4a16.5 16.5 0 0 0 0 4zm.8 2h2.9a15.7 15.7 0 0 0 1.4 3.6A8 8 0 0 1 5.1 16zM8 8H5.1a8 8 0 0 1 4.3-3.6A15.7 15.7 0 0 0 8 8zm4 12a14 14 0 0 1-1.9-4h3.8A14 14 0 0 1 12 20zm2.3-6H9.7a14.7 14.7 0 0 1 0-4h4.6a14.7 14.7 0 0 1 0 4zm.3 5.6a15.7 15.7 0 0 0 1.4-3.6h2.9a8 8 0 0 1-4.3 3.6zM16.3 14a16.5 16.5 0 0 0 0-4h3.4a8 8 0 0 1 0 4z"/></svg>
        www.crestlinelending.com
      </li>
      <li>
        <svg viewBox="0 0 24 24" aria-hidden="true"><path d="M3 5h18a1 1 0 0 1 1 1v12a1 1 0 0 1-1 1H3a1 1 0 0 1-1-1V6a1 1 0 0 1 1-1zm9 7.2L4.5 7.3V17h15V7.3z"/></svg>
        info@crestlinelending.com
      </li>
    </ul>

    <div class="person">
      <p class="person-name"><span class="first">Jane</span> <span class="last">Doe</span></p>
      <p class="person-title">Branch Manager</p>
    </div>
    <div class="edge-tab" aria-hidden="true"></div>
  </section>

  <section class="card card-back" aria-label="Card back">
    <div class="brand">
      <span class="brand-dot"></span>
      <span class="brand-name">Crestline Lending Group</span>
    </div>

    <div class="referral">
      <p class="referral-lead">Refer a Friend</p>
      <div class="referral-offer">
        <span class="referral-get">GET</span>
        <span class="referral-upto">UP<br>TO</span>
      </div>
      <p class="referral-amount">$100</p>
    </div>

    <div class="divider" aria-hidden="true"></div>

    <div class="services">
      <p class="services-title">SERVICES</p>
      <ul>
        <li>Title Loans</li>
        <li>Tax Services</li>
        <li>Personal Loans</li>
      </ul>
    </div>
  </section>

</body>
</html>
```